Million Dollar Vehicle Design For Home Service Company

New design for Brightway Tradesmen (home service company) vehicles.

Both sides and back

We are a new (opening in about 30 days) home service company.

We will begin by offering residential electrical services and soon expand to a full line by adding handyman, heating, cooling. plumbing and drain cleaning.

Looking for simple. Not cluttered.

Minimalist - Less is More mindset, but it must catch the eye.

Here is a link the website prototype being built for us. It has a bit more stuff on it now than it will in its final version, but this will help you get a feel for the colors.

http://www.lanternquay.com/PROOF/brightway-tradesmen-4/

You may also find inspiration at sunnymarsh.com

**Also, please note that some of the attached files will differ from my requests due to changes being made as we get closer to opening. For example, the tagline is different.

Target Market(s)

Home Owners 35 - 65 years old.

Industry/Entity Type

Electrician

Font styles to use
Serif

Requirements
Must have
• Simple. Easy to read. Easy to understand what the company does and how to contact.
• Big Website
• Big Phone Number
• Big Name
• Website: GoBrightwayFix.com
• Phone number: 515-555-0187
• ***Tagline: Brightway, All the Way or You'll Save $39
• ***Please note the tagline in this brief is different than is in the attached image.
Nice to have
• We will be adding services in the future. It would be nice to consider how these will be displayed on the vehicle. For example, it should be listed that we provide expert electrical services. I want to be able to list other services such as plumbing, heating and cooling as we add them by modifying only few things on each vehicle.
Should not have
• Cluttered. Should not be difficult to understand within 1 second.

```html
<!DOCTYPE html>
<html lang="en">
<head>
<meta charset="utf-8">
<title>Brightway Tradesmen – Vehicle Wrap Side</title>
<link href="https://fonts.googleapis.com/css2?family=Passion+One:wght@700&family=Montserrat:wght@700;800;900&display=swap" rel="stylesheet">
<style>
  :root {
    --charcoal: #3a3b3c;
    --charcoal-deep: #2b2c2d;
    --orange: #e8532f;
    --orange-soft: #f07a55;
    --white: #ffffff;
    --green: #5cb531;
    --denim: #2f4fa8;
  }
  html, body {
    margin: 0;
    width: 1200px;
    height: 797px;
    overflow: hidden;
    background: var(--white);
  }
  .wrap-side {
    display: block;
    width: 1200px;
    height: 797px;
  }
  .wrap-base { fill: var(--charcoal); }
  .accent-band { fill: var(--orange); }
  .services-band { fill: var(--white); }
  .speed-line { fill: none; stroke: var(--white); stroke-width: 5; stroke-linecap: round; }
  .brand-name {
    font-family: "Passion One", sans-serif;
    font-weight: 700;
    font-size: 88px;
    fill: var(--white);
    stroke: var(--charcoal-deep);
    stroke-width: 5;
    paint-order: stroke;
  }
  .brand-sub {
    font-family: "Montserrat", sans-serif;
    font-weight: 900;
    font-size: 36px;
    fill: var(--charcoal);
  }
  .trade-box { fill: var(--charcoal); stroke: var(--white); stroke-width: 4; }
  .trade-label {
    font-family: "Montserrat", sans-serif;
    font-weight: 800;
    font-size: 31px;
    fill: var(--white);
  }
  .tagline {
    font-family: "Montserrat", sans-serif;
    font-weight: 800;
    font-size: 18px;
    fill: var(--white);
  }
  .tagline .saving { fill: var(--green); }
  .web-band { fill: var(--white); }
  .website {
    font-family: "Montserrat", sans-serif;
    font-weight: 900;
    font-size: 31px;
    fill: var(--charcoal);
  }
  .phone {
    font-family: "Montserrat", sans-serif;
    font-weight: 900;
    font-size: 46px;
    fill: var(--white);
  }
  .phone-icon { fill: var(--orange); }
  .service {
    font-family: "Montserrat", sans-serif;
    font-weight: 900;
    font-size: 25px;
  }
  .service.dark { fill: var(--charcoal); }
  .service.bright { fill: var(--orange); }
</style>
</head>
<body>
<svg class="wrap-side" viewBox="0 0 1200 797" xmlns="http://www.w3.org/2000/svg">
  <defs>
    <linearGradient id="technician-tone" x1="0" y1="0" x2="0" y2="1">
      <stop offset="0" stop-color="#e8532f"/>
      <stop offset="0.55" stop-color="#f07a55"/>
      <stop offset="1" stop-color="#2f4fa8"/>
    </linearGradient>
  </defs>

  <rect class="wrap-base" x="0" y="0" width="1200" height="797"/>

  <polygon class="accent-band" points="40,320 1200,40 1200,300 40,600"/>
  <polygon class="services-band" points="975,150 1200,90 1200,400 975,460"/>

  <path class="speed-line" d="M18 520 Q30 400 58 360"/>
  <path class="speed-line" d="M30 570 Q42 460 58 420"/>

  <rect class="technician" x="62" y="110" width="190" height="610" rx="36"
        fill="url(#technician-tone)" role="img"
        aria-label="Illustrated female electrician in orange cap and shirt holding a tablet"/>
  <rect class="technician" x="790" y="90" width="170" height="560" rx="36"
        fill="url(#technician-tone)" role="img"
        aria-label="Illustrated male electrician in orange cap giving a thumbs up with a coil of cable"/>

  <g class="brand-block" transform="rotate(-8 515 330)">
    <text class="brand-name" x="292" y="232">BRIGHTWAY</text>
    <text class="brand-sub" x="298" y="282">TRADESMEN</text>
    <rect class="trade-box" x="298" y="298" width="290" height="52" rx="4"/>
    <text class="trade-label" x="314" y="335">ELECTRICIANS</text>
    <text class="tagline" x="312" y="380">Brightway, All the Way</text>
    <text class="tagline" x="312" y="404">or You'll Save <tspan class="saving">$39</tspan>!</text>

    <polygon class="web-band" points="286,430 672,430 664,480 278,480"/>
    <text class="website" x="294" y="467">GoBrightwayFix.com</text>

    <path class="phone-icon" d="M296 512 h30 a6 6 0 0 1 6 6 v5 h-9 l-4 -5 h-16 l-4 5 h-9 v-5 a6 6 0 0 1 6 -6z M294 527 h34 l4 18 h-42z"/>
    <text class="phone" x="342" y="546">515-555-0187</text>
  </g>

  <g class="services-list" transform="rotate(-8 1088 280)">
    <text class="service dark" x="998" y="225">ELECTRICAL</text>
    <text class="service bright" x="1008" y="262">PLUMBING</text>
    <text class="service dark" x="1018" y="299">HEATING</text>
    <text class="service bright" x="1026" y="336">COOLING</text>
  </g>
</svg>
</body>
</html>
```